Create for us a Shop-Stopper Business Card

We need a standout, first class business card to go along with our new brand strategy. Sleek, Contemporary and fresh.

Colors and theme must sync with our websitewww.pelvorpower.co.uk

We want a business card that has a global brand appeal. TKR Energy is a small UK renewable company that specialises in energy projects in Africa. We want a business card that has the following characteristics: Very short, precise, global, stand out, NOT TOO LOUD but contemporary. The company's colour themes are White, Grey with a hint of green.

Target Market(s)

Business exec, high net worth individuals, investors, commercial leaders, suppliers, government officials

Industry/Entity Type

Solar Energy

Contact Information for Business Card

Logo, Name, Title, Address, web address, email,

Requirements
Must have
• Logo must be sharp
Nice to have
• Adapt fonts from the logo. The large circular side of the logo at the back in a very refreshing way
Should not have
• No solar panel shapes or image.Very little black. If possible avoid black. Its not coming out nice. I think !!!

```html
<!DOCTYPE html>
<html lang="en">
<head>
<meta charset="utf-8">
<title>TKR Energy – Business Card</title>
<link rel="stylesheet" href="https://fonts.googleapis.com/css2?family=Montserrat:wght@400;500;600&display=swap">
<style>
  :root {
    --backdrop: #bcbdbf;
    --card-white: #ffffff;
    --card-charcoal: #333331;
    --brand-green: #0f7438;
    --fresh-green: #8cc63f;
    --ink: #2b2b2b;
    --paper-text: #f2f2f2;
  }
  * { box-sizing: border-box; margin: 0; padding: 0; }
  html, body {
    width: 1200px; height: 927px; overflow: hidden;
    background: var(--backdrop);
    font-family: "Montserrat", Arial, sans-serif;
  }
  .card {
    position: absolute; top: 190px;
    width: 315px; height: 550px;
    border-radius: 16px;
    text-align: center;
  }
  .card--front { left: 243px; background: var(--card-white); color: var(--ink); }
  .card--back { left: 645px; background: var(--card-charcoal); color: var(--paper-text); }

  .brand-mark {
    position: absolute; left: 66px; top: 48px;
    width: 180px; height: 180px;
  }
  .brand-mark__name {
    font-family: "Montserrat", Arial, sans-serif;
    font-weight: 600; font-size: 22px; letter-spacing: 1px;
    fill: var(--brand-green);
  }

  .holder { position: absolute; left: 0; right: 0; top: 332px; }
  .holder__name { font-size: 24px; font-weight: 500; color: var(--brand-green); line-height: 28px; }
  .holder__title { font-size: 13.5px; line-height: 17px; }
  .holder__address { margin-top: 9px; font-size: 14px; line-height: 19.5px; }
  .contact-icons { margin-top: 8px; height: 14px; display: flex; justify-content: center; gap: 5px; }
  .contact-icons svg { width: 12px; height: 12px; stroke: var(--brand-green); fill: none; stroke-width: 1.4; }
  .contact-list { margin-top: 4px; font-size: 14px; line-height: 19.5px; }
  .contact-list .domain { color: var(--brand-green); }

  .back-logo {
    position: absolute; left: 26px; top: 251px;
    display: flex; align-items: center; gap: 9px;
  }
  .back-logo__dot { width: 48px; height: 48px; border-radius: 50%; background: var(--brand-green); }
  .back-logo__name { font-size: 30px; font-weight: 500; letter-spacing: 0.5px; color: var(--paper-text); }

  .tagline {
    position: absolute; left: 0; right: 0; top: 428px;
    font-size: 15px; font-weight: 500; letter-spacing: 0.6px; color: var(--fresh-green);
  }
  .social { position: absolute; left: 0; right: 0; top: 458px; display: flex; justify-content: center; gap: 9px; }
  .social span { width: 22px; height: 22px; border-radius: 50%; background: var(--paper-text); }
  .back-web { position: absolute; left: 0; right: 0; top: 489px; font-size: 14.5px; letter-spacing: 0.3px; }
</style>
</head>
<body>
  <section class="card card--front" aria-label="Business card front">
    <svg class="brand-mark" viewBox="0 0 180 180" role="img" aria-label="TKR Energy brand mark">
      <circle cx="90" cy="90" r="81" fill="none" stroke="var(--brand-green)" stroke-width="16"/>
      <text class="brand-mark__name" x="90" y="98" text-anchor="middle">TKR Energy</text>
    </svg>

    <div class="holder">
      <h1 class="holder__name">Marlo Fenwick</h1>
      <p class="holder__title">Director</p>
      <p class="holder__address">48 Brackenford Lane<br>Halvergate, NR 4120</p>
      <div class="contact-icons" aria-hidden="true">
        <svg viewBox="0 0 12 12"><path d="M3 1.5 L4.5 4 L3.5 5 Q5 7.5 7 8.5 L8 7.5 L10.5 9 L9.5 10.5 Q4 10 1.5 3 Z"/></svg>
        <svg viewBox="0 0 12 12"><rect x="1" y="2.5" width="10" height="7" rx="1"/><path d="M1.5 3 L6 6.5 L10.5 3"/></svg>
        <svg viewBox="0 0 12 12"><circle cx="6" cy="6" r="4.8"/><ellipse cx="6" cy="6" rx="2" ry="4.8"/><path d="M1.2 6 H10.8 M2 3.5 H10 M2 8.5 H10"/></svg>
      </div>
      <p class="contact-list">
        +004 3185-2094<br>
        info@pelvorpower.co.uk<br>
        www.<span class="domain">pelvorpower</span>.co.uk
      </p>
    </div>
  </section>

  <section class="card card--back" aria-label="Business card back">
    <div class="back-logo">
      <span class="back-logo__dot" aria-hidden="true"></span>
      <span class="back-logo__name">TKR ENERGY</span>
    </div>
    <p class="tagline">LET'S DO THE IMPOSSIBLE</p>
    <div class="social" aria-label="Social media links">
      <span></span><span></span><span></span>
    </div>
    <p class="back-web">www.pelvorpower.co.uk</p>
  </section>
</body>
</html>
```